K12 Online Learning Landing Page

We provide an Elearning site for K12 learners. I would like to redesign the landing page. The design should have a responsive view too. So I'm looking for designs that encompass the Login requirements and other links and buttons. I have attached images of the current landing page.

Target Market(s)

K12 Learners

Industry/Entity Type

Education, Training or Edtech

Font styles to use
Sans Serif

Colors

Designer to choose colors to be used in the design.

Requirements
Must have
• Login Area
Nice to have
• Menu Area, area for notices or infomation

```html
<!DOCTYPE html>
<html lang="en">
<head>
<meta charset="utf-8">
<title>Brightpath Education – Login and Landing Page</title>
<link href="https://fonts.googleapis.com/css2?family=Lato:wght@400;700&family=Montserrat:wght@600;700&family=Dancing+Script:wght@500;600&display=swap" rel="stylesheet">
<style>
:root{
  --page-bg:#d3dce4;
  --panel-light:#eef1f3;
  --brand:#2b64a4;
  --brand-dark:#1f5592;
  --brand-mid:#3a80cf;
  --brand-soft:#7eaad8;
  --brand-pale:#b9d0ea;
  --ink:#2f3a44;
  --ink-soft:#5a6570;
  --white:#ffffff;
  --go:#4ec63b;
  --shop:#c5281f;
  --line:#c8d0d8;
}
*{box-sizing:border-box;margin:0;padding:0}
html,body{width:1200px;height:4073px;overflow:hidden}
body{background:var(--page-bg);font-family:'Lato',Arial,sans-serif;color:var(--ink);position:relative}
.abs{position:absolute}

/* ---------- Login screen ---------- */
.login-screen{left:76px;top:74px;width:1051px;height:655px;background:var(--panel-light);overflow:hidden}
.login-visual{left:0;top:0}
.brand-mark{font-family:'Lato',Arial,sans-serif;font-weight:700;color:var(--brand);line-height:1}
.login-logo{left:440px;top:70px;width:200px;text-align:right}
.login-logo .name{font-size:42px;display:block}
.login-logo .sub{font-size:20px;display:block;margin-top:6px}
.login-title{top:181px;width:327px;text-align:center;font-size:16px;color:var(--ink)}
.field{left:628px;width:327px;height:50px;border:1px solid var(--line);border-radius:4px;background:var(--white);font-size:15px;color:#8a949d;padding:0 20px;display:flex;align-items:center}
.btn-block{left:628px;width:327px;height:49px;border-radius:4px;color:var(--white);font-size:15px;letter-spacing:.5px;display:flex;align-items:center;justify-content:center}
.btn-login{top:348px;background:var(--brand)}
.btn-video{top:454px;background:var(--go)}
.btn-shop{top:509px;background:var(--shop)}
.login-divider{left:628px;top:425px;width:327px;height:1px;background:#b8c1c9}
.forgot{left:628px;top:575px;width:327px;text-align:center;font-size:16px;color:var(--brand)}

/* ---------- Landing page ---------- */
.landing{left:77px;top:795px;width:1053px;height:3186px;background:var(--white);overflow:hidden}
.topbar{left:0;top:0;width:100%;height:38px;background:var(--brand-mid)}
.topbar .mail{left:98px;top:0;height:38px;display:flex;align-items:center;gap:12px;color:var(--white);font-size:13px}
.topbar .links{left:735px;top:0;height:38px;display:flex;align-items:center;color:var(--white);font-size:12px;gap:8px;letter-spacing:.3px}
.topbar .search{left:936px;top:11px}

.navbar{left:0;top:38px;width:100%;height:73px;background:var(--white)}
.nav-logo{left:98px;top:7px}
.nav-logo .name{font-size:34px;display:block}
.nav-logo .sub{font-size:14px;display:block;text-align:right;margin-top:2px;color:var(--ink)}
.nav-menu{left:349px;top:0;height:73px;display:flex;align-items:center;gap:24px;font-size:15px;color:var(--ink);list-style:none}
.nav-menu .active{color:var(--brand-mid);position:relative}
.nav-menu .active::before{content:"";position:absolute;left:50%;top:-14px;width:8px;height:8px;margin-left:-4px;border-radius:50%;background:var(--brand-mid)}
.btn{display:flex;align-items:center;justify-content:center;border-radius:5px;font-size:15px;letter-spacing:.4px;color:var(--white)}
.btn-solid{background:var(--brand-mid)}
.btn-outline{border:2px solid var(--white)}
.nav-cta{left:824px;top:16px;width:131px;height:43px;background:var(--brand)}

.hero{left:0;top:111px;width:100%;height:600px}
.hero-eyebrow{left:98px;top:150px;font-size:15px;color:var(--white);letter-spacing:.3px}
.hero-title{left:98px;top:195px;font-family:'Montserrat',Arial,sans-serif;font-weight:700;font-size:44px;line-height:57px;color:var(--white)}
.hero-book{left:98px;top:344px;width:130px;height:43px}
.hero-trial{left:239px;top:344px;width:174px;height:43px}
.hero-arrow{top:244px}

.section-title{font-family:'Dancing Script',cursive;font-weight:600;font-size:38px;display:flex;align-items:center;gap:18px;white-space:nowrap}
.section-title .rule{display:block;width:48px;height:2px}
.title-on-white{color:var(--ink)}
.title-on-white .rule{background:var(--ink)}
.title-on-white em{font-style:normal;color:var(--brand-mid)}
.title-on-blue{color:var(--white)}
.title-on-blue .rule{background:var(--white)}
.centered{left:0;width:100%;justify-content:center}

.about-visual{left:49px;top:760px}
.about-title{left:535px;top:758px}
.about-copy{left:535px;top:832px;width:418px;font-size:14.5px;line-height:27px;color:var(--ink);text-align:justify}
.about-copy p+p{margin-top:16px}
.about-book{left:535px;top:1025px;width:131px;height:42px}

.video-band{left:0;top:1145px;width:100%;height:735px;background:var(--brand)}
.video-frame{left:101px;top:1298px;width:852px;height:433px;border:2px solid var(--white);border-radius:8px;overflow:hidden;background:linear-gradient(160deg,#8d8a84 0%,#6d6a64 45%,#4f4c48 100%)}
.video-heading{left:0;top:14px;width:100%;text-align:center;font-family:'Montserrat',Arial,sans-serif;font-weight:600;font-size:41px;line-height:55px;color:var(--white)}
.video-play{left:397px;top:188px}
.video-join{left:431px;top:1785px;width:191px;height:44px;border:1.5px solid #cfe1f5;background:var(--brand-mid);font-size:14px}

.courses-title{top:1942px}
.course-card{top:2058px;width:254px;height:367px;border:1px solid #d5dbe1;border-radius:6px;background:var(--white);overflow:hidden}
.course-card.featured{box-shadow:0 10px 22px rgba(30,60,90,.22);border-color:#e2e6ea}
.course-art{display:block;width:100%;height:237px}
.course-name{margin-top:34px;text-align:center;font-size:15px;font-weight:700;letter-spacing:.4px;color:var(--brand)}
.course-grade{margin-top:6px;text-align:center;font-size:15px;color:var(--ink)}
.course-link{margin-top:12px;text-align:center;font-size:14px;font-weight:700;color:var(--brand-mid);text-decoration:underline;letter-spacing:.3px}
.carousel-arrow{top:2208px}

.signup-band{left:0;top:2498px;width:100%;height:514px;background:var(--brand)}
.signup-title{top:2553px}
.signup-intro{left:98px;top:2634px;width:860px;font-size:14.5px;line-height:26px;color:var(--white)}
.signup-steps{left:98px;top:2722px;width:500px;list-style:none;color:var(--white);font-size:14.5px;line-height:27px}
.signup-steps li{position:relative;padding-left:32px}
.signup-steps li::before{content:"";position:absolute;left:2px;top:10px;width:8px;height:8px;border-radius:50%;background:var(--white)}
.signup-steps li+li{margin-top:30px}
.signup-steps li:last-child{margin-top:14px}
.signup-book{left:98px;top:2913px;width:131px;height:42px;border:1.5px solid #cfe1f5;background:var(--brand-mid)}
.signup-visual{left:601px;top:2744px}

.footer-logo{left:98px;top:3035px}
.footer-logo .name{font-size:50px;display:block}
.footer-logo .sub{font-size:20px;display:block;text-align:right;margin-top:4px;color:var(--ink)}
.social{left:794px;top:3054px;display:flex;gap:14px}
.social span{display:block;width:20px;height:20px;border-radius:50%;background:var(--brand-mid)}
.footer-nav{left:0;top:3092px;width:953px;display:flex;justify-content:flex-end;gap:24px;font-size:14.5px;color:var(--ink);list-style:none}
.footer-rule{left:98px;top:3135px;width:855px;height:1px;background:#d8dde2}
.copyright{left:0;top:3156px;width:100%;text-align:center;font-size:13px;color:var(--ink)}
</style>
</head>
<body>

<!-- Login screen -->
<section class="abs login-screen" aria-label="Login screen">
  <svg class="abs login-visual" width="640" height="655" viewBox="0 0 640 655" role="img" aria-label="Photo of a student writing in a notebook at a laptop, set against a curved blue doodle-pattern backdrop">
    <defs>
      <linearGradient id="loginBlue" x1="0" y1="0" x2="1" y2="1">
        <stop offset="0" stop-color="#2c65a5"/>
        <stop offset="1" stop-color="#1d4f8c"/>
      </linearGradient>
      <linearGradient id="loginPhoto" x1="0" y1="0" x2="0" y2="1">
        <stop offset="0" stop-color="#3a6ea9" stop-opacity="0"/>
        <stop offset="0.35" stop-color="#b98a4e" stop-opacity="0.55"/>
        <stop offset="0.75" stop-color="#d8c3a4"/>
        <stop offset="1" stop-color="#e7e3dd"/>
      </linearGradient>
      <clipPath id="loginCurve">
        <path d="M0,105 C70,60 170,55 235,130 C300,210 330,330 400,405 C470,480 560,540 610,655 L0,655 Z"/>
      </clipPath>
    </defs>
    <g clip-path="url(#loginCurve)">
      <rect width="640" height="655" fill="url(#loginBlue)"/>
      <rect x="0" y="150" width="640" height="505" fill="url(#loginPhoto)"/>
    </g>
  </svg>

  <div class="abs brand-mark login-logo"><span class="name">Brightpath</span><span class="sub">Education</span></div>
  <p class="abs login-title" style="left:628px">Login or Create Account</p>
  <div class="abs field" style="top:229px">Email or Phone number</div>
  <div class="abs field" style="top:289px">Password</div>
  <div class="abs btn-block btn-login">LOGIN</div>
  <div class="abs login-divider"></div>
  <div class="abs btn-block btn-video">VIEW HOW TO VIDEO</div>
  <div class="abs btn-block btn-shop">SHOP</div>
  <p class="abs forgot">Forgot your Password?</p>
</section>

<!-- Landing page -->
<main class="abs landing" aria-label="Landing page">

  <div class="abs topbar">
    <div class="abs mail">
      <svg width="16" height="12" viewBox="0 0 16 12" aria-hidden="true"><rect x="0.5" y="0.5" width="15" height="11" rx="1" fill="none" stroke="#fff"/><path d="M1,1 L8,7 L15,1" fill="none" stroke="#fff"/></svg>
      <span>hello@brightpathlearn.example</span>
    </div>
    <div class="abs links"><span>LOG IN</span><span>|</span><span>SIGN UP</span><span>|</span><span>USER</span></div>
    <svg class="abs search" width="16" height="16" viewBox="0 0 16 16" aria-hidden="true"><circle cx="6.5" cy="6.5" r="5" fill="none" stroke="#fff" stroke-width="1.6"/><path d="M10.3,10.3 L15,15" stroke="#fff" stroke-width="1.6"/></svg>
  </div>

  <nav class="abs navbar">
    <div class="abs brand-mark nav-logo"><span class="name">Brightpath</span><span class="sub">Education</span></div>
    <ul class="abs nav-menu">
      <li class="active">Home</li><li>About</li><li>Popular Courses</li><li>Why choose us?</li><li>Contact</li>
    </ul>
    <div class="abs btn nav-cta">CONTACT US</div>
  </nav>

  <section class="abs hero" aria-label="Welcome">
    <svg class="abs" style="left:0;top:0" width="1053" height="600" viewBox="0 0 1053 600" aria-hidden="true">
      <defs>
        <linearGradient id="heroBlue" x1="0" y1="0" x2="0" y2="1">
          <stop offset="0" stop-color="#2b62a3"/>
          <stop offset="1" stop-color="#2f6cb0"/>
        </linearGradient>
      </defs>
      <rect width="1053" height="600" fill="url(#heroBlue)"/>
      <path d="M0,520 C140,410 260,400 380,440 C520,490 640,420 780,400 C900,385 980,420 1053,440 L1053,600 L0,600 Z" fill="#4b86c6"/>
      <path d="M0,560 C160,450 300,440 430,470 C580,505 700,470 840,470 C940,470 1000,500 1053,520 L1053,600 L0,600 Z" fill="#7ea9d7"/>
      <path d="M0,600 C90,520 170,470 280,475 C420,482 540,545 700,560 C840,572 960,560 1053,545 L1053,600 Z" fill="#ffffff"/>
    </svg>
    <div class="abs" style="left:616px;top:100px;width:300px;height:440px;border-radius:150px 150px 40px 40px;background:linear-gradient(180deg,#5b86b8 0%,#e9eef3 40%,#3c5b86 100%);opacity:.9" role="img" aria-label="Photo of a smiling student sitting cross-legged with a laptop"></div>
    <p class="abs hero-eyebrow">THE MODERN LEARNING EXPERIENCE</p>
    <h1 class="abs hero-title">Welcome to the<br>Brightpath LMS</h1>
    <div class="abs btn btn-solid hero-book">BOOK NOW</div>
    <div class="abs btn btn-outline hero-trial">REQUEST TRIAL</div>
    <svg class="abs hero-arrow" style="left:38px" width="18" height="34" viewBox="0 0 18 34" aria-hidden="true"><path d="M16,2 L2,17 L16,32" fill="none" stroke="#fff" stroke-width="2"/></svg>
    <svg class="abs hero-arrow" style="left:997px" width="18" height="34" viewBox="0 0 18 34" aria-hidden="true"><path d="M2,2 L16,17 L2,32" fill="none" stroke="#fff" stroke-width="2"/></svg>
  </section>

  <svg class="abs about-visual" width="420" height="310" viewBox="0 0 420 310" role="img" aria-label="Laptop showing the Brightpath platform home screen inside a pale blue circle">
    <circle cx="155" cy="150" r="145" fill="#b9d0ea"/>
    <circle cx="50" cy="250" r="45" fill="#ffffff" stroke="#b9d0ea" stroke-width="3"/>
    <rect x="107" y="40" width="230" height="205" rx="8" fill="#1e2530"/>
    <rect x="117" y="50" width="210" height="185" fill="#eef3fa"/>
    <rect x="70" y="245" width="300" height="8" rx="4" fill="#9aa3ad"/>
  </svg>
  <h2 class="abs section-title title-on-white about-title">About <em>Brightpath</em><span class="rule"></span></h2>
  <div class="abs about-copy">
    <p>Experience breakthrough learning with a platform that offers Grade 4-12 CAPS curriculum Maths and Science training through personal, interactive sessions at any pace.</p>
    <p>Watch tutorials and get in touch with educators including group chats to post your questions. Choose from a variety of question sheets and quizzes to test your knowledge as you go.</p>
  </div>
  <div class="abs btn btn-solid about-book">BOOK NOW</div>

  <section class="abs video-band" aria-label="Course videos"></section>
  <h2 class="abs section-title title-on-blue centered" style="top:1196px"><span class="rule"></span>Watch our course videos<span class="rule"></span></h2>
  <div class="abs video-frame" role="img" aria-label="Video still of a student with headphones at a laptop in a kitchen, with cartoon learners on either side">
    <p class="abs video-heading">Brightpath Learning Management<br>System</p>
    <svg class="abs video-play" width="54" height="38" viewBox="0 0 54 38" aria-hidden="true"><circle cx="27" cy="19" r="18" fill="#ffffff"/><path d="M22,11 L35,19 L22,27 Z" fill="#2b64a4"/></svg>
  </div>
  <div class="abs btn video-join">JOIN LIVE SESSIONS</div>

  <h2 class="abs section-title title-on-white centered courses-title"><span class="rule"></span>Our <em>Popular Courses</em><span class="rule"></span></h2>
  <svg class="abs carousel-arrow" style="left:36px" width="18" height="34" viewBox="0 0 18 34" aria-hidden="true"><path d="M16,2 L2,17 L16,32" fill="none" stroke="#3a80cf" stroke-width="2"/></svg>
  <svg class="abs carousel-arrow" style="left:997px" width="18" height="34" viewBox="0 0 18 34" aria-hidden="true"><path d="M2,2 L16,17 L2,32" fill="none" stroke="#3a80cf" stroke-width="2"/></svg>

  <article class="abs course-card" style="left:98px">
    <div class="course-art" role="img" aria-label="Chalkboard flyer with geometry sketches for live mathematics sessions" style="background:linear-gradient(160deg,#3a3d40,#1f2224)"></div>
    <h3 class="course-name">LIVE MATHEMATICS</h3>
    <p class="course-grade">Grade 7,9 &amp; 11</p>
    <p class="course-link">REQUEST TRIAL</p>
  </article>
  <article class="abs course-card featured" style="left:400px">
    <div class="course-art" role="img" aria-label="Red and white flyer with a stack of books for live mathematics sessions" style="background:linear-gradient(180deg,#eeeeee 0%,#eeeeee 38%,#e0312b 42%,#d7261f 100%)"></div>
    <h3 class="course-name">LIVE MATHEMATICS</h3>
    <p class="course-grade">Grade 8, 10 &amp; 12</p>
    <p class="course-link">REQUEST TRIAL</p>
  </article>
  <article class="abs course-card" style="left:700px">
    <div class="course-art" role="img" aria-label="Green chalkboard flyer with science sketches for natural and physical science sessions" style="background:linear-gradient(160deg,#3f5a48,#26392d)"></div>
    <h3 class="course-name">NATURAL &amp; PHYSICAL Sc</h3>
    <p class="course-grade">Grade 7,9 &amp; 11</p>
    <p class="course-link">REQUEST TRIAL</p>
  </article>

  <section class="abs signup-band" aria-label="Signing up"></section>
  <h2 class="abs section-title title-on-blue centered signup-title"><span class="rule"></span>Signing Up<span class="rule"></span></h2>
  <p class="abs signup-intro">It's never too late to get ahead of the game. Make the most of your Connectel subscription and access Brightpath Education for free, today. Now with lessons for learners from Grade 4 - 12.</p>
  <ul class="abs signup-steps">
    <li>Sign up and create a username and password</li>
    <li>Browse the site and find the tutorials and videos that suit your needs.</li>
    <li>Learn at your own pace and log in to the site whenever you want to,<br>to pick up where you left off.</li>
  </ul>
  <div class="abs btn signup-book">BOOK NOW</div>
  <div class="abs signup-visual" style="width:439px;height:268px;background:linear-gradient(180deg,rgba(255,255,255,0) 0%,#c9d6e2 45%,#f2f2ef 100%);border-radius:120px 0 0 0" role="img" aria-label="Photo of a learner at a desk working on a desktop computer with a lamp beside it"></div>

  <div class="abs brand-mark footer-logo"><span class="name">Brightpath</span><span class="sub">Education</span></div>
  <div class="abs social" aria-label="Social links"><span></span><span></span><span></span><span></span><span></span></div>
  <ul class="abs footer-nav">
    <li>Home</li><li>About</li><li>Popular Courses</li><li>Why choose us?</li><li>Contact</li>
  </ul>
  <div class="abs footer-rule"></div>
  <p class="abs copyright">2022 Brightpath Education. All Rights Reserved.</p>
</main>

</body>
</html>
```